Business Card Design for Vel
Fun, earthy, organic food company needs professional cards to speak our message!
Business Card Design for Vel -
Creative Brief
Bright & Fun-filled
Marcus Dell
Managing Member & Co-Founder
PO Box 482937 Dallas, TX 75318-2937
mdell@ourvelway.com
http:\\www.ourvelway.com
If you can access the closed project, we'll be using logo #84 in the folowing link: http://www.kavdrafthub.com/contests/logo-for-vel. We'll be uploading the logo file shortly for this project. We like simple, fun and creative but are open to many designs and styles.
The back of the card should be our logo colors, green and brown. It could be a cool design based off of the colors, you could use the entire length of the back with the logo or place both colors on the back with it being split with a similar design of the tree in our logo. We're open to your creativity!
quelldraw quelldraw
@KR - working on it now & submit our conmcepts soon! Thanks
Fovra Fovra
Please Check top right message box of the page.
trolen447 trolen447
Designers, We're looking to expedite the process on this. First come first serve on the card design. If you provide designs for stationary as well and we choose you, we'll provide a $50 donation to you. We're even open to selecting two winners for business card and stationary. So submit for each, because you could win for either or both! Thanks!

```html
<!DOCTYPE html>
<html lang="en">
<head>
<meta charset="utf-8">
<title>Vel — Business Card</title>
<link rel="stylesheet" href="https://fonts.googleapis.com/css2?family=PT+Sans:wght@400;700&display=swap">
<style>
  :root {
    --backdrop: #ece9e4;
    --card: #ffffff;
    --leaf-green: #8cc63f;
    --earth-brown: #3d2414;
    --ink: #3a3a3a;
    --divider: #d6d6d6;
  }
  * { margin: 0; padding: 0; box-sizing: border-box; }
  html, body {
    width: 1200px;
    height: 780px;
    overflow: hidden;
    background: var(--backdrop);
    font-family: "PT Sans", Arial, sans-serif;
  }
  .card {
    position: absolute;
    left: 100px;
    top: 104px;
    width: 1000px;
    height: 571px;
    background: var(--card);
    border-radius: 34px;
    overflow: hidden;
    box-shadow: 0 10px 30px rgba(0, 0, 0, 0.18);
  }
  .brand {
    position: absolute;
    left: 130px;
    top: 96px;
    width: 240px;
    display: flex;
    flex-direction: column;
    align-items: center;
  }
  .brand-square {
    width: 240px;
    height: 240px;
    background: var(--earth-brown);
  }
  .brand-name {
    margin-top: 18px;
    font-size: 36px;
    font-weight: 700;
    line-height: 1.1;
    color: var(--ink);
  }
  .divider {
    position: absolute;
    left: 410px;
    top: 90px;
    width: 2px;
    height: 340px;
    background: var(--divider);
  }
  .details {
    position: absolute;
    left: 445px;
    top: 88px;
    color: var(--ink);
  }
  .person-name {
    font-size: 36px;
    font-weight: 700;
    color: var(--leaf-green);
    line-height: 1.1;
  }
  .person-title {
    margin-top: 6px;
    font-size: 22px;
    line-height: 1.25;
  }
  .address {
    margin-top: 56px;
    font-size: 22px;
    line-height: 1.3;
  }
  .contacts {
    margin-top: 28px;
    list-style: none;
    font-size: 21px;
    line-height: 1.45;
  }
  .contacts li {
    display: flex;
    align-items: center;
    gap: 12px;
  }
  .contacts svg {
    width: 18px;
    height: 18px;
    flex: none;
  }
  .bottom-bands {
    position: absolute;
    left: 0;
    bottom: 0;
    width: 1000px;
    height: 120px;
  }
</style>
</head>
<body>
  <main class="card">
    <div class="brand">
      <div class="brand-square"></div>
      <div class="brand-name">Vel</div>
    </div>

    <div class="divider"></div>

    <section class="details">
      <h1 class="person-name">Marcus Dell</h1>
      <p class="person-title">Managing Member &amp;<br>Co-Founder</p>
      <p class="address">PO Box 482937<br>Dallas, TX 75318-2937</p>
      <ul class="contacts">
        <li>
          <svg viewBox="0 0 20 20" aria-hidden="true"><path fill="var(--leaf-green)" d="M5 2l3 4-2 2c1 2 3 4 5 5l2-2 4 3-2 3C9 17 3 11 2 5z"/></svg>
          817-555-0147
        </li>
        <li>
          <svg viewBox="0 0 20 20" aria-hidden="true"><rect x="2" y="4" width="16" height="12" rx="1" fill="var(--leaf-green)"/><path d="M2 5l8 6 8-6" fill="none" stroke="#fff" stroke-width="1.5"/></svg>
          mdell@ourvelway.com
        </li>
        <li>
          <svg viewBox="0 0 20 20" aria-hidden="true"><circle cx="10" cy="10" r="8" fill="var(--leaf-green)"/><path d="M2 10h16M10 2c-3 3-3 13 0 16M10 2c3 3 3 13 0 16" fill="none" stroke="#fff" stroke-width="1.2"/></svg>
          www.ourvelway.com
        </li>
      </ul>
    </section>

    <svg class="bottom-bands" viewBox="0 0 1000 120" aria-hidden="true">
      <polygon fill="var(--leaf-green)" points="0,94 660,62 620,120 0,120"/>
      <polygon fill="var(--earth-brown)" points="620,120 660,62 1000,30 1000,120"/>
    </svg>
  </main>
</body>
</html>
```